Craft Instant Coffee Box Packaging design

We need packaging designed for our craft instant coffee. Needs to be simple yet eye-catching. We are looking to package instant coffee sachets inside a cigarette style box. Front of box must make it clear that it is instant coffee and show contents - 7 pack / 21g net as well as Brindle Oak Coffee Co. which is the company name. We'd prefer the instant coffee be the focal point rather than the company name. The rear will have 'ingredients', company address and barcode. Sides should either state contents such as 'Instant Coffee' or company name.

Font styles to use
Sans Serif

Colors

Designer to choose colors to be used in the design.

Requirements
Must have
• Front of box must make it clear that it is instant coffee and show contents - 7 pack / 21g net as well as Brindle Oak Coffee Co. which is the company name. We'd prefer the instant coffee be the focal point rather than the company name. The rear will have 'ingredients', company address and barcode. Sides should either state contents such as 'Instant Coffee' or company name.
Nice to have
• modern colour scheme - 'Brindle Oak Coffee Co.' in a simple sans serif font
Should not have
• Must not be too 'busy' or 'cheap' looking

```html
<!DOCTYPE html>
<html lang="en">
<head>
<meta charset="utf-8">
<title>Brindle Oak Coffee Co. – Instant Coffee Box Front</title>
<link rel="stylesheet" href="https://fonts.googleapis.com/css2?family=Montserrat:wght@400;500&display=swap">
<style>
  :root {
    --backdrop: #c9cfd0;
    --box-black: #0d0d0d;
    --ink-white: #f2f2f2;
    --cup-grey: #5a5a5a;
  }
  html, body {
    margin: 0;
    padding: 0;
    width: 1200px;
    height: 789px;
    overflow: hidden;
    background: var(--backdrop);
  }
  .canvas {
    width: 1200px;
    height: 789px;
    display: flex;
    align-items: center;
    justify-content: center;
  }
  .box-front {
    width: 430px;
    height: 660px;
    background: var(--box-black);
    box-sizing: border-box;
    display: flex;
    flex-direction: column;
    align-items: center;
    color: var(--ink-white);
    font-family: "Montserrat", sans-serif;
  }
  .brand-name {
    margin-top: 84px;
    display: flex;
    align-items: center;
    gap: 10px;
    font-weight: 500;
    font-size: 17px;
    letter-spacing: 3px;
    text-transform: uppercase;
  }
  .brand-mark {
    width: 10px;
    height: 10px;
    background: var(--ink-white);
  }
  .product-name {
    margin-top: 40px;
    font-weight: 500;
    font-size: 36px;
    letter-spacing: 4px;
    text-transform: uppercase;
    line-height: 1;
    white-space: nowrap;
  }
  .cup-illustration {
    margin-top: 62px;
    width: 190px;
    height: 160px;
    border-radius: 0 0 90px 90px;
    background: radial-gradient(circle at 50% 40%, #6a6a6a, var(--cup-grey) 70%);
  }
  .contents {
    margin-top: 62px;
    text-align: center;
    font-weight: 500;
  }
  .contents-count {
    font-size: 17px;
    letter-spacing: 5px;
    text-transform: uppercase;
  }
  .contents-weight {
    margin-top: 22px;
    font-size: 15px;
    letter-spacing: 1px;
  }
</style>
</head>
<body>
  <main class="canvas">
    <section class="box-front">
      <div class="brand-name"><span class="brand-mark"></span>Brindle Oak Coffee Co.</div>
      <h1 class="product-name" style="margin-bottom:0;">Instant Coffee</h1>
      <div class="cup-illustration" role="img" aria-label="Grey steaming coffee cup illustration"></div>
      <div class="contents">
        <div class="contents-count">Pack of Seven</div>
        <div class="contents-weight">21g</div>
      </div>
    </section>
  </main>
</body>
</html>
```